A website for a Maltese Law Firm

Our law firm needs a website to further its business. The site should have a simple yet effective design. We would need the following sections: About us, Practice Areas, About Malta, Contact. These should be further split as follows:

About us: Our firm, Our values, What others say, Offices

Practice Areas: Crimimal, Citizenship & Residence, Harbour Passage Scheme, Criminal Defence, Civil Litigation, Arbitration and ADR, Commercial and Corporate, Media Law.

About Malta: just one section.

Contact: Just one section

We would also need a news feed at the front of the site to include latest news regarding our cases.

At the bottom we need a section for our Terms and a Privacy Statement.

Our logo is being attached.

Target Market(s)

All clients looking for legal assistance in Malta

Industry/Entity Type

Legal

Coding

Coded - Design and coding required

Number of Pages Required

1 page

Requirements
Must have
• It must be simple yet striking.

```html
<!DOCTYPE html>
<html lang="en">
<head>
<meta charset="utf-8">
<title>Calleja &amp; Rizzo</title>
<link rel="stylesheet" href="https://fonts.googleapis.com/css2?family=Cinzel:wght@400&family=Questrial&display=swap">
<style>
:root{
  --ink:#111;
  --text:#555;
  --muted:#888;
  --line:#d9d9d9;
  --footer:#1d1d1d;
  --footer-text:#bbb;
  --white:#fff;
}
*{margin:0;padding:0;box-sizing:border-box}
h1,h2,h3,h4,h5{font-weight:400}
html,body{width:1200px;height:3061px;overflow:hidden;background:var(--white)}
body{position:relative;font-family:"Questrial",sans-serif;color:var(--text)}
.abs{position:absolute}
.top-rule{left:0;top:0;width:1200px;height:4px;background:#bdbdbd}
.brand{left:0;width:1200px;top:40px;display:flex;justify-content:center;align-items:center;gap:10px;font-family:"Questrial",sans-serif;font-size:24px;color:var(--ink);line-height:1}
.brand-mark{width:12px;height:12px;background:var(--ink)}
.nav{left:170px;top:105px;width:860px;height:34px;border-top:1px solid var(--line);border-bottom:1px solid var(--line)}
.nav a{position:absolute;top:8px;font-size:13px;color:#333;text-decoration:none}
.hero{left:0;top:139px;width:1200px;height:377px;background:linear-gradient(180deg,#fafafa 0%,#eee 55%,#cfcfcf 100%)}
.tagline{left:582px;top:224px;font-family:"Cinzel",serif;font-size:17px;letter-spacing:1px;color:var(--ink);white-space:nowrap}
.section-title{left:0;width:1200px;text-align:center;font-family:"Cinzel",serif;font-size:27px;letter-spacing:1.5px;color:#222;line-height:34px}
.title-rule{left:585px;width:30px;height:2px;background:var(--ink)}
.lead{left:200px;width:800px;text-align:center;font-size:12.5px;line-height:18px;color:var(--muted)}
.btn{width:96px;height:26px;background:var(--ink);color:var(--white);font-size:12px;text-align:center;line-height:26px;left:552px}
.practice-band{left:0;top:828px;width:1200px;height:487px;background:linear-gradient(120deg,#d8d8d8,#ececec 45%,#dcdcdc)}
.practice-grid{left:163px;top:960px;width:870px;height:310px;display:grid;grid-template-columns:repeat(4,1fr);grid-template-rows:repeat(2,1fr);border:1px solid #c8c8c8;background:rgba(255,255,255,.35)}
.practice{border-right:1px solid #c8c8c8;border-bottom:1px solid #c8c8c8;text-align:center;padding-top:36px}
.practice:nth-child(4n){border-right:none}
.practice:nth-child(n+5){border-bottom:none}
.practice svg{display:block;margin:0 auto 12px}
.practice h3{font-size:13px;color:#222}
.practice p{font-size:12px;color:#666;margin-top:7px}
.divider{left:170px;top:1640px;width:860px;height:1px;background:var(--line)}
.card{background:var(--white);border:1px solid var(--line);width:268px}
.photo{display:block;width:100%}
.card-body{padding:14px}
.card-head{display:flex;gap:10px;align-items:flex-start}
.card-head svg{flex:none}
.card-head h4{font-size:14px;color:#222;line-height:17px}
.meta{font-size:10.5px;color:#444;margin:12px 0 10px 34px}
.excerpt{font-size:11px;line-height:15px;color:var(--muted)}
.quote{font-size:14px;line-height:17px;color:#222}
.cite{font-size:12px;color:var(--muted);margin:12px 0 0 34px;line-height:15px}
.dots{left:578px;top:2309px;display:flex;gap:8px}
.dots span{width:7px;height:7px;border-radius:50%;background:#bbb}
.dots span:first-child{background:#333}
.map{left:0;top:2354px;width:1200px;height:372px;background:#e6e6e6}
.map-info{left:393px;top:2428px;width:182px;height:78px;background:#111;color:#eee;font-size:10.5px;line-height:15px;padding:8px 10px}
.footer{left:0;top:2726px;width:1200px;height:335px;background:var(--footer)}
.f-head{top:2785px;font-family:"Cinzel",serif;font-size:16px;letter-spacing:1px;color:#ddd}
.f-text{font-size:11px;line-height:17px;color:var(--footer-text);text-align:justify}
.field{left:396px;width:192px;height:18px;border:1px solid #444;background:#252525;color:#777;font-size:10px;line-height:16px;padding-left:6px}
.submit{left:396px;top:2943px;width:60px;height:17px;background:var(--white);color:#111;font-size:10px;text-align:center;line-height:17px}
.social{left:836px;top:2847px;display:flex;gap:8px}
.social span{width:22px;height:22px;background:#3b3b3b}
.f-bottom{left:175px;top:3020px;width:850px;height:1px;background:#333}
.copy{left:175px;top:3026px;font-size:10px;color:#777}
.f-brand{left:840px;top:3026px;width:176px;display:flex;justify-content:flex-end;align-items:center;gap:7px;font-family:"Questrial",sans-serif;font-size:15px;color:#ddd;line-height:1}
.f-brand i{width:8px;height:8px;background:#ddd}
</style>
</head>
<body>
<div class="abs top-rule"></div>

<header>
  <div class="abs brand"><span class="brand-mark"></span><span>Calleja &amp; Rizzo</span></div>
  <nav class="abs nav">
    <a style="left:143px">About us</a>
    <a style="left:258px">Practice Areas &#8964;</a>
    <a style="left:423px">About Malta</a>
    <a style="left:568px">News</a>
    <a style="left:661px">Contact</a>
  </nav>
</header>

<div class="abs hero" role="img" aria-label="Black and white photograph of chess pieces, two white kings before a row of black pawns"></div>
<div class="abs tagline">Integrity &nbsp;·&nbsp; Committed &nbsp;·&nbsp; Ethical</div>

<section>
  <h2 class="abs section-title" style="top:558px">About us</h2>
  <div class="abs title-rule" style="top:608px"></div>
  <p class="abs lead" style="top:646px">Lorem ipsum dolor sit amet, consectetur adipiscing elit, sed do eiusmod tempor incid idunt ut labore et dolore magna aliqua. Ut enim ad minim veniam, quis nostrud exerc itat ion ullamco laboris nisi ut aliquip ex ea commodo consequat. Duis aute irure dolor in repren enderit in voluptate velit esse cillum dolore eu fugiat nulla pariatur. Excepteur sint occaecat cupidatat non proident, sunt in culpa qui officia deserunt mollit anim id est laborum.</p>
  <div class="abs btn" style="top:758px">Read More</div>
</section>

<section>
  <div class="abs practice-band" role="img" aria-label="Faded photograph of the scales of justice and a judge's gavel"></div>
  <h2 class="abs section-title" style="top:864px">Practice Areas</h2>
  <div class="abs title-rule" style="top:915px"></div>
  <div class="abs practice-grid">
    <div class="practice"><svg width="28" height="28"><rect width="28" height="28" fill="#111"/><circle cx="14" cy="14" r="6" fill="none" stroke="#fff" stroke-width="1.6"/></svg><h3>Criminal</h3><p>85 jobs done</p></div>
    <div class="practice"><svg width="28" height="28"><rect width="28" height="28" fill="#111"/><path d="M7 14l7-6 7 6v7H7z" fill="none" stroke="#fff" stroke-width="1.6"/></svg><h3>Citizenship &amp; Residence</h3><p>67 jobs done</p></div>
    <div class="practice"><svg width="28" height="28"><rect width="28" height="28" fill="#111"/><rect x="8" y="9" width="12" height="10" fill="none" stroke="#fff" stroke-width="1.6"/></svg><h3>Harbour Passage Scheme</h3><p>47 jobs done</p></div>
    <div class="practice"><svg width="28" height="28"><rect width="28" height="28" fill="#111"/><path d="M14 7v14M8 10h12M8 10l-2 6h4zM20 10l-2 6h4z" fill="none" stroke="#fff" stroke-width="1.4"/></svg><h3>Criminal Defence</h3><p>61 jobs done</p></div>
    <div class="practice"><svg width="28" height="28"><rect width="28" height="28" fill="#111"/><path d="M8 20l8-8M13 9l6 6" stroke="#fff" stroke-width="2"/><path d="M7 22h10" stroke="#fff" stroke-width="1.6"/></svg><h3>Civil Litigation</h3><p>72 jobs done</p></div>
    <div class="practice"><svg width="28" height="28"><rect width="28" height="28" fill="#111"/><circle cx="10" cy="11" r="3" fill="#fff"/><circle cx="18" cy="11" r="3" fill="#fff"/><path d="M6 21c0-4 8-4 8 0M14 21c0-4 8-4 8 0" fill="#fff"/></svg><h3>Arbitration and ADR</h3><p>98 jobs done</p></div>
    <div class="practice"><svg width="28" height="28"><rect width="28" height="28" fill="#111"/><rect x="7" y="11" width="14" height="10" fill="none" stroke="#fff" stroke-width="1.6"/><path d="M11 11V8h6v3" fill="none" stroke="#fff" stroke-width="1.6"/></svg><h3>Commercial and Corporate</h3><p>37 jobs done</p></div>
    <div class="practice"><svg width="28" height="28"><rect width="28" height="28" fill="#111"/><circle cx="13" cy="13" r="5" fill="none" stroke="#fff" stroke-width="1.6"/><path d="M17 17l4 4" stroke="#fff" stroke-width="2"/></svg><h3>Media Law</h3><p>44 jobs done</p></div>
  </div>
</section>

<section>
  <h2 class="abs section-title" style="top:1354px">About Malta</h2>
  <div class="abs title-rule" style="top:1402px"></div>
  <p class="abs lead" style="top:1435px">Sed quia consequuntur magni dolores eos qui ratione voluptatem sequi nesciunt. Neque porro quisquam est, qui dolorem ipsum quia dolor sit amet, consectetur, adipisci velit, sed quia non numquam eius modi tempora incidunt ut labore et dolore magnam aliquam quaerat voluptatem. Ut enim ad minima veniam, quis nostrum exercitationem ullam corporis suscipit laboriosam, nisi ut aliquid ex ea commodi consequatur? Quis autem vel eum iure reprehenderit qui in ea voluptate velit esse quam nihil molestiae consequatur, vel illum qui dolorem eum fugiat quo voluptas nulla pariatur</p>
  <div class="abs btn" style="top:1564px">Read More</div>
  <div class="abs divider"></div>
</section>

<section>
  <h2 class="abs section-title" style="top:1678px">Latest From Feeds</h2>
  <div class="abs title-rule" style="top:1729px"></div>

  <article class="abs card" style="left:173px;top:1773px">
    <div class="photo" style="height:135px;background:linear-gradient(135deg,#6b4a25,#c9934f 50%,#f0e2c8)" role="img" aria-label="Photograph of a brass scale and a gavel"></div>
    <div class="card-body">
      <div class="card-head"><svg width="22" height="22"><rect x=".5" y=".5" width="21" height="21" fill="none" stroke="#bbb"/><path d="M7 15l7-7 1.5 1.5-7 7H7z" fill="#444"/></svg><h4>Dipisci velit, sed quia non num quam eius modi</h4></div>
      <div class="meta">&#9638; Jun 07.2016 &nbsp; &#9679; No Comments</div>
      <p class="excerpt">Dignissimos ducimus qui blanditiis prae sentium voluptatum deleniti tque corr upti quos dolores filam libero tempore[...]</p>
    </div>
  </article>
  <article class="abs card" style="left:173px;top:2105px">
    <div class="card-body">
      <div class="card-head"><svg width="22" height="22"><rect x=".5" y=".5" width="21" height="21" fill="none" stroke="#bbb"/><rect x="7" y="7" width="8" height="8" fill="#444"/></svg><h4>Ut enim ad minima veniam placeat facere possi</h4></div>
      <div class="meta">&#9638; Jan 18.2016 &nbsp; &#9679; 5 Comments</div>
      <p class="excerpt">Mnis dolor repellendus. Temporibus autem quibusdam et aut officiis debitis aut rerum necessitatibus[...]</p>
    </div>
  </article>

  <article class="abs card" style="left:464px;top:1773px">
    <div class="card-body">
      <div class="card-head"><svg width="22" height="22"><rect x=".5" y=".5" width="21" height="21" fill="none" stroke="#bbb"/><text x="6" y="17" font-size="14" font-family="serif" font-weight="700" fill="#444">“</text></svg><p class="quote">“Sed quia consequuntur mag dolores eos qui ratione volu em sequi nesciunt.”</p></div>
      <p class="cite">- Mara Vella<br><small>Chief Justice</small></p>
    </div>
  </article>
  <article class="abs card" style="left:464px;top:1930px">
    <div class="card-body">
      <div class="card-head"><svg width="22" height="22"><rect x=".5" y=".5" width="21" height="21" fill="none" stroke="#bbb"/><rect x="6" y="8" width="7" height="6" fill="#444"/><path d="M13 11l4-3v6z" fill="#444"/></svg><h4>Cum soluta nobis est</h4></div>
      <p class="excerpt" style="margin-top:12px">Repellendus def emporibus autem quib usdam et aut.</p>
    </div>
    <div style="height:148px;background:linear-gradient(180deg,#5a3a22,#8a5a33 60%,#2a1a10);position:relative" role="img" aria-label="Video still of a courtroom session">
      <div style="position:absolute;left:0;bottom:0;width:100%;height:18px;background:#111"></div>
    </div>
  </article>

  <article class="abs card" style="left:759px;top:1773px">
    <div class="photo" style="height:135px;background:linear-gradient(90deg,#3a1e12,#6e3a22 40%,#2a2a2a 70%,#8a6a4a)" role="img" aria-label="Photograph of a row of bound law books"></div>
    <div class="card-body">
      <div class="card-head"><svg width="22" height="22"><rect x=".5" y=".5" width="21" height="21" fill="none" stroke="#bbb"/><path d="M7 15l7-7 1.5 1.5-7 7H7z" fill="#444"/></svg><h4>Dipisci velit, sed quia non num quam eius modi</h4></div>
      <div class="meta">&#9638; Jun 07.2016 &nbsp; &#9679; 15 Comments</div>
      <p class="excerpt">Dignissimos ducimus qui blanditiis prae sentium voluptatum deleniti tque corr upti quos dolores Nam libero tempore[...]</p>
    </div>
  </article>
  <article class="abs card" style="left:759px;top:2095px">
    <div class="card-body">
      <div class="card-head"><svg width="22" height="22"><rect x=".5" y=".5" width="21" height="21" fill="none" stroke="#bbb"/><rect x="7" y="7" width="8" height="8" fill="#444"/></svg><p class="quote">“At vero eos et accusamus et iusto odio dignissimos ducimus qui blanditiis praeseti.”</p></div>
      <p class="cite">- Paul Deguara<br><small>Ass.-Chief Justice</small></p>
    </div>
  </article>

  <div class="abs dots"><span></span><span></span><span></span></div>
</section>

<section>
  <div class="abs map" role="img" aria-label="Greyscale street map of central Malta from Birkirkara to Valletta"></div>
  <svg class="abs" style="left:405px;top:2516px" width="16" height="22"><path d="M8 21C3 14 1 11 1 8a7 7 0 0 1 14 0c0 3-2 6-7 13z" fill="#e0262b"/><circle cx="8" cy="8" r="2.6" fill="#fff"/></svg>
  <svg class="abs" style="left:958px;top:2463px" width="16" height="22"><path d="M8 21C3 14 1 11 1 8a7 7 0 0 1 14 0c0 3-2 6-7 13z" fill="#e0262b"/><circle cx="8" cy="8" r="2.6" fill="#fff"/></svg>
  <div class="abs" style="left:419px;top:2538px;font-size:12px;color:#222">Birkirkara</div>
  <div class="abs" style="left:940px;top:2485px;font-size:12px;color:#222">Valletta</div>
  <div class="abs map-info">&#9679; 12, Triq il-Ġnien, Birkirkara<br>&#9742; (356) 2000 1480 (Birkirkara)<br>&#9636; (356) 2000 1481<br>&#9993; info@callejarizzo.example</div>
</section>

<footer>
  <div class="abs footer"></div>
  <h5 class="abs f-head" style="left:175px">About Us</h5>
  <p class="abs f-text" style="left:175px;top:2835px;width:190px">Lorem ipsum dolor sit amet, consectetur adipiscing elit, sed do eiusmod tempor incididunt ut labore et dolore magna aliqua. Ut enim ad minim veniam, quis nostrud exercitation ullamco laboris nisi ut aliquip ex ea commodo.</p>

  <h5 class="abs f-head" style="left:396px">Stay Connected</h5>
  <div class="abs field" style="top:2840px">Your name...</div>
  <div class="abs field" style="top:2862px">Your mail address...</div>
  <div class="abs field" style="top:2884px;height:46px">Leave us a message...</div>
  <div class="abs submit">SUBMIT</div>

  <h5 class="abs f-head" style="left:616px">Links</h5>
  <p class="abs f-text" style="left:616px;top:2838px;text-align:left">Terms &amp; Conditions<br>Privacy Policy<br>News<br>Services</p>

  <h5 class="abs f-head" style="left:836px">Follow Us</h5>
  <div class="abs social"><span></span><span></span><span></span><span></span></div>

  <div class="abs f-bottom"></div>
  <p class="abs copy">Copyright © Calleja &amp; Rizzo 2016</p>
  <div class="abs f-brand"><i></i><span>Calleja &amp; Rizzo</span></div>
</footer>
</body>
</html>
```